Lantern Signs Facebook Banner Design

Design a facebook banner for a sign company. I would like to have a modern approach to it.

Product Offering:
Signs
Banners
Decals
Commercial Wraps

```html
<!DOCTYPE html>
<html lang="en">
<head>
<meta charset="UTF-8">
<title>Lantern Signs – Facebook Banner</title>
<link href="https://fonts.googleapis.com/css2?family=Poppins:wght@400;600;700&display=swap" rel="stylesheet">
<style>
  :root {
    --backdrop: #666666;
    --paper: #ffffff;
    --warm-tint: #fff8ec;
    --brand-red: #ee3238;
    --brand-red-soft: #f6a6a3;
    --ink: #474747;
    --mist: #d9d9d7;
    --mug-light: #f4f4f4;
    --mug-shade: #d6d6d6;
    --bottle-light: #2e74c4;
    --bottle-dark: #1f3f86;
  }
  * { margin: 0; padding: 0; box-sizing: border-box; }
  html, body {
    width: 1200px; height: 684px; overflow: hidden;
    background: var(--backdrop);
    font-family: "Poppins", sans-serif;
  }
  .banner {
    position: absolute;
    left: 98.6px; top: 132.9px;
    width: 1200px; height: 500px;
    transform: scale(0.8357);
    transform-origin: 0 0;
    overflow: hidden;
    background: radial-gradient(ellipse at 45% 85%, var(--warm-tint) 0%, var(--paper) 60%);
  }
  .decor { position: absolute; inset: 0; }
  .wordmark {
    position: absolute;
    left: 600px; top: 118px;
    transform: translateX(-50%);
    text-align: center;
    color: var(--ink);
    font-weight: 700;
    text-transform: uppercase;
    font-size: 54px;
    line-height: 1.05;
    letter-spacing: 1px;
    white-space: nowrap;
  }
  .offering-title {
    position: absolute;
    left: 600px; top: 332px;
    transform: translateX(-50%);
    display: flex; align-items: center; gap: 12px;
    color: var(--ink);
    font-size: 42px; font-weight: 400;
    white-space: nowrap;
  }
  .offering-title .rule {
    width: 78px; height: 3px;
    background: linear-gradient(90deg, rgba(238,50,56,0.1), var(--brand-red));
  }
  .offering-title .rule.right {
    background: linear-gradient(90deg, var(--brand-red), rgba(238,50,56,0.1));
  }
  .offering-list {
    position: absolute;
    left: 600px; top: 404px;
    transform: translateX(-50%);
    display: flex; align-items: center; gap: 20px;
    list-style: none;
    color: var(--ink);
    font-size: 27px; font-weight: 400;
    text-transform: uppercase;
    white-space: nowrap;
  }
  .offering-list .dot {
    width: 11px; height: 11px; border-radius: 50%;
    background: var(--brand-red);
  }
  .product-mug {
    position: absolute;
    left: 17px; top: 306px; width: 190px; height: 166px;
    border-radius: 10px 40px 40px 10px;
    background: linear-gradient(90deg, var(--mug-light), var(--mug-shade));
  }
  .product-bottle {
    position: absolute;
    left: 992px; top: 19px; width: 110px; height: 372px;
    border-radius: 20px 20px 8px 8px;
    background: linear-gradient(90deg, var(--bottle-light), var(--bottle-dark));
  }
</style>
</head>
<body>
  <section class="banner">
    <svg class="decor" width="1200" height="500" viewBox="0 0 1200 500" aria-hidden="true">
      <circle cx="-10" cy="160" r="250" fill="var(--mist)" opacity="0.85"/>
      <circle cx="-120" cy="480" r="290" fill="var(--brand-red)"/>
      <circle cx="1085" cy="140" r="252" fill="var(--brand-red-soft)"/>
      <circle cx="1092" cy="136" r="234" fill="var(--brand-red)"/>
    </svg>

    <div class="wordmark">Lantern<br>Signs</div>

    <h2 class="offering-title">
      <span class="rule"></span>Product Offering<span class="rule right"></span>
    </h2>

    <ul class="offering-list">
      <li>Signs</li><li class="dot"></li>
      <li>Banners</li><li class="dot"></li>
      <li>Decals</li><li class="dot"></li>
      <li>Commercial Wraps</li>
    </ul>

    <div class="product-mug" role="img" aria-label="White branded coffee mug with company name"></div>
    <div class="product-bottle" role="img" aria-label="Blue metal water bottle with company name printed vertically"></div>
  </section>
</body>
</html>
```